Can you make our site AWESOME?

Hi Guys,

I am a co-founder of Tipper Crate Rentals Australia, the world's first e-commerce skip bin business.

We are looking to update our site before a launch into the UK in March.

Please help us by submitting your designs for the following pages:

- Home page (www.tippercraterentals-example.com.au)
- About us (https://www.tippercraterentals-example.com.au/pages/about-us
- Contact us (https://www.tippercraterentals-example.com.au/pages/contact-us)
- Quick Quote / Pricing (https://www.tippercraterentals-example.com.au/pages/free-instant-quote-skip-bin-hire)

NOTES:
- Design should be high-converting
- best designs will be fresh, modern, easy to read, distinctive and memorable
- please use our logo and video colours
- feel free to change logos, layout, images and anything else you feel can be improved
- the winning designer will potentially have the opportunity to re-design the other pages on our site
- brief is for design only

Any questions just ask.

Thanks,
Oliver

```html
<!DOCTYPE html>
<html lang="en">
<head>
<meta charset="utf-8">
<title>Tipper Crate Rentals Australia</title>
<link href="https://fonts.googleapis.com/css2?family=Roboto:wght@300;400;500;700&display=swap" rel="stylesheet">
<style>
  :root {
    --green: #6aa847;
    --green-dark: #1e7a34;
    --teal: #1d5c56;
    --teal-soft: #6e938d;
    --tile: rgba(236, 236, 236, 0.88);
    --tile-text: #1f5b56;
    --band: #eef0ec;
    --quote: #bccfc9;
    --white: #ffffff;
    --nav-btn: #6b6b6b;
  }
  * { box-sizing: border-box; margin: 0; padding: 0; }
  html, body { width: 1200px; height: 1200px; overflow: hidden; }
  body { font-family: "Roboto", sans-serif; background: var(--white); position: relative; }

  .hero { position: absolute; left: 0; top: 0; width: 1200px; height: 528px; }
  .hero-photo {
    position: absolute; inset: 0;
    background: linear-gradient(100deg, #b9d6ee 0%, #6d8ca8 25%, #3f5466 50%, #2a2d33 75%, #0b0b0c 100%);
  }
  .hero-photo::after {
    content: ""; position: absolute; left: 0; right: 0; bottom: 0; height: 60%;
    background: linear-gradient(180deg, rgba(150,110,70,0) 0%, rgba(120,90,60,0.35) 100%);
  }
  .nav { position: absolute; left: 0; top: 0; width: 1200px; height: 68px; color: var(--white); }
  .brand { position: absolute; left: 180px; top: 22px; font-size: 11px; font-weight: 700; letter-spacing: 0.5px; line-height: 1.15; width: 120px; }
  .brand small { display: block; font-size: 7px; letter-spacing: 5px; font-weight: 700; }
  .phone { position: absolute; left: 312px; top: 27px; font-size: 10px; display: flex; align-items: center; gap: 3px; }
  .menu a { position: absolute; top: 28px; font-size: 10px; color: #d4d4d4; text-decoration: none; font-weight: 300; }
  .menu a.active { color: var(--white); font-weight: 400; }
  .nav-cta { position: absolute; left: 934px; top: 21px; width: 88px; height: 25px; background: var(--nav-btn); color: #eee; font-size: 9px; display: flex; align-items: center; justify-content: center; }

  .hero-title { position: absolute; left: 180px; top: 118px; font-size: 30px; font-weight: 400; color: var(--white); }
  .hero-sub { position: absolute; left: 180px; top: 172px; width: 380px; font-size: 15.5px; font-weight: 300; color: var(--white); line-height: 1.25; }
  .quote-title { position: absolute; left: 614px; top: 128px; font-size: 16px; font-weight: 500; color: var(--white); }
  .quote-input { position: absolute; left: 614px; top: 164px; width: 290px; height: 29px; background: #f1f1f1; display: flex; align-items: center; justify-content: space-between; padding: 0 8px 0 12px; font-size: 10px; color: #999; }
  .or { position: absolute; left: 614px; top: 209px; font-size: 15px; color: var(--white); }
  .btn { position: absolute; background: var(--green); color: var(--white); font-size: 14px; display: flex; align-items: center; justify-content: center; }
  .hero .btn { left: 614px; top: 245px; width: 119px; height: 40px; }

  .segments { position: absolute; left: 398px; top: 450px; display: flex; gap: 1px; }
  .segment { width: 80px; height: 78px; background: var(--tile); display: flex; flex-direction: column; align-items: center; justify-content: flex-end; padding-bottom: 9px; color: var(--tile-text); font-size: 14px; gap: 6px; }
  .segment svg { width: 36px; height: 32px; }

  .steps-title { position: absolute; left: 180px; top: 567px; font-size: 27px; color: var(--teal); font-weight: 400; }
  .rule { position: absolute; height: 1px; background: var(--green); opacity: 0.7; }
  .steps-intro { position: absolute; left: 180px; top: 621px; width: 360px; font-size: 14px; line-height: 1.22; color: var(--teal-soft); }
  .step-icon { position: absolute; }
  .step-title { position: absolute; left: 247px; font-size: 12.5px; color: var(--teal); }
  .step-text { position: absolute; left: 248px; width: 290px; font-size: 10.5px; line-height: 1.65; color: var(--teal-soft); }
  .video { position: absolute; left: 618px; top: 672px; width: 408px; height: 238px; background: radial-gradient(circle at 50% 55%, #63b36b 0%, #1c6e2c 45%, #1e7d33 100%); }
  .steps .btn { left: 247px; top: 974px; width: 149px; height: 40px; }

  .reviews { position: absolute; left: 0; top: 1048px; width: 1200px; height: 152px; background: var(--band); overflow: hidden; }
  .quote-mark { position: absolute; left: 238px; top: -30px; font-size: 300px; line-height: 1; color: var(--quote); font-weight: 700; font-family: "Roboto", sans-serif; }
  .reviews h2 { position: absolute; left: 0; width: 1200px; top: 52px; text-align: center; font-size: 25px; font-weight: 400; color: var(--teal); }
  .reviews p { position: absolute; left: 0; width: 1200px; top: 108px; text-align: center; font-size: 12px; color: var(--teal-soft); }
</style>
</head>
<body>
<header class="hero">
  <div class="hero-photo" role="img" aria-label="Photo of a crew of tradespeople building a timber roof frame against a blue sky"></div>
  <nav class="nav">
    <div class="brand">TIPPER CRATE RENTALS<small>AUSTRALIA</small></div>
    <div class="phone">
      <svg width="11" height="11" viewBox="0 0 24 24"><path fill="#fff" d="M6.6 10.8a15 15 0 0 0 6.6 6.6l2.2-2.2c.3-.3.7-.4 1-.2 1.1.4 2.3.6 3.6.6.6 0 1 .4 1 1V20c0 .6-.4 1-1 1A17 17 0 0 1 3 4c0-.6.4-1 1-1h3.5c.6 0 1 .4 1 1 0 1.3.2 2.5.6 3.6.1.3 0 .7-.2 1z"/></svg>
      1800 555 019
    </div>
    <div class="menu">
      <a class="active" style="left:633px" href="#">HOME</a>
      <a style="left:698px" href="#">ABOUT</a>
      <a style="left:762px" href="#">LEARN MORE</a>
      <a style="left:855px" href="#">CONTACT</a>
    </div>
    <div class="nav-cta">Call Us Now</div>
  </nav>
  <h1 class="hero-title">Skip Hire Tailored For Tradies</h1>
  <p class="hero-sub">From Australia's fastest growing Skip Bin Hire company.Easy bookings, great service, lowest prices, T&amp;C's designed for you.</p>
  <div class="quote-title">Get Instant Quote</div>
  <div class="quote-input">Enter Postcode or Suburb
    <svg width="15" height="15" viewBox="0 0 24 24"><circle cx="10" cy="10" r="6.5" fill="none" stroke="#333a4a" stroke-width="2.4"/><path d="M15 15l6 6" stroke="#333a4a" stroke-width="2.8"/></svg>
  </div>
  <div class="or">Or</div>
  <div class="btn">Call Us Now</div>
  <div class="segments">
    <div class="segment"><svg viewBox="0 0 36 32" fill="none" stroke="#6aa847" stroke-width="1.4"><path d="M3 15L18 3l15 12"/><path d="M7 12v18h22V12"/><rect x="11" y="17" width="6" height="6"/><rect x="20" y="17" width="5" height="13"/></svg>Renovator</div>
    <div class="segment"><svg viewBox="0 0 36 32" fill="none" stroke="#6aa847" stroke-width="1.4"><path d="M3 18h30l-4 7H7z"/><rect x="8" y="9" width="20" height="9"/><path d="M8 13.5h20M14 9v9M20 9v9M3 28c3-2 6 2 9 0s6 2 9 0 6 2 9 0"/></svg>Tradie</div>
    <div class="segment"><svg viewBox="0 0 36 32" fill="none" stroke="#6aa847" stroke-width="1.4"><path d="M4 4h28M10 4v26M24 4v6"/><rect x="13" y="12" width="14" height="18"/><path d="M17 16v3M22 16v3M17 23v3M22 23v3M2 30h32"/></svg>Builder</div>
    <div class="segment"><svg viewBox="0 0 36 32" fill="none" stroke="#6aa847" stroke-width="1.4"><rect x="4" y="9" width="28" height="20" rx="1"/><path d="M13 9V5h10v4M4 17h28"/><rect x="16" y="15" width="4" height="5"/></svg>Corporate</div>
    <div class="segment"><svg viewBox="0 0 36 32" fill="none" stroke="#6aa847" stroke-width="1.4"><path d="M3 16l4-8 8-2 3 4 4-7 3 7 7 6-2 10-8 2-5-3-6 1-8-4z"/></svg>National</div>
  </div>
</header>

<section class="steps">
  <h2 class="steps-title">Easy As 1,2,3..</h2>
  <div class="rule" style="left:180px; top:613px; width:57px;"></div>
  <p class="steps-intro">We manage your booking from start to finish, so you can focus on other things</p>

  <svg class="step-icon" style="left:181px; top:705px" width="40" height="24" viewBox="0 0 40 24" fill="none" stroke="#6aa847" stroke-width="1.5"><path d="M2 5h36l-5 12H9z"/><path d="M6 5l3-3h22l3 3"/><path d="M9 17l2 5h18l2-5"/></svg>
  <div class="step-title" style="top:695px">Easy Booking</div>
  <p class="step-text" style="top:722px">Call 1800 555 019 or click here to get started with your instant quote</p>

  <svg class="step-icon" style="left:183px; top:788px" width="35" height="26" viewBox="0 0 35 26" fill="none" stroke="#6aa847" stroke-width="1.5"><rect x="1" y="1" width="33" height="24"/><path d="M1 1l16.5 14L34 1M1 25l12-11M34 25L22 14"/></svg>
  <div class="step-title" style="left:248px; top:779px">Instant Confirmation</div>
  <p class="step-text" style="left:249px; top:806px; width:300px">Receive your booking details and a 30 minute courtesy call before drop off</p>

  <svg class="step-icon" style="left:186px; top:868px" width="44" height="26" viewBox="0 0 44 26" fill="none" stroke="#6aa847" stroke-width="1.5"><rect x="1" y="1" width="26" height="18"/><path d="M27 7h9l6 7v5H27z"/><circle cx="9" cy="22" r="3" fill="#fff"/><circle cx="34" cy="22" r="3" fill="#fff"/></svg>
  <div class="step-title" style="top:863px">Gone When You Are Ready</div>
  <p class="step-text" style="top:887px">Let us know and your bin will be gone within 24hrs</p>

  <div class="video" role="img" aria-label="Video thumbnail: best service across Australia, map of delivery routes with a play button"></div>
  <div class="btn">Call Us Now</div>
</section>

<section class="reviews">
  <div class="quote-mark">”</div>
  <h2>Reviews</h2>
  <div class="rule" style="left:573px; top:96px; width:54px;"></div>
  <p>Five Star Service</p>
</section>
</body>
</html>
```